Postcard Flyer For Plumbing Company

We are a p[professional plumbing company in NSW that carry out plumbing, electrical and hot water system work.
i want to send a postcard size flyer 105mm x 148mm to our clients to offer $xx off their next job they book with us.
The front of the flyer needs to say.... Feel The Love WIth $35 Off your Next Job. It needs to include a section where their name and postal address can go (74mm W x 24mm H) on the left hand side of the bottom of the flyer - refer attached example.
The other side of the flyer needs to have a section for text, the offer ($35 or $xx what they get off their next job) and also can use the tag line... Call 1 Number for The Best In 3 Trades - Plumbing, Hot Water & Electrical.
Plumbing, hot water and electrical pictures/icons can be used.
I want the flyer to stand out, use the corporate colours and be modern whilst letting them know that they can use this voucher on their next job.
Refer attachments.

Target Market(s)

Homeowners and our existing clients

Industry/Entity Type

Plumbing

Font styles to use
Serif

Colors
0255a3
ec1f27
ffffff
d3d3d3

Requirements
Must have
• Corporate colours and logos
• Red Colour:
• C=0
• M=100
• Y=100
• K=0
• Blue Colour
• C= 100
• M=66
• Y=0
• K=2
• Grey Colour
• C= 26
• M=21
• Y=19
• K=0
Nice to have
• predominately white background
Should not have
• Black background and lots of black.

```html
<!DOCTYPE html>
<html lang="en">
<head>
<meta charset="utf-8">
<title>Harbour Trades – Postcard Flyer</title>
<link rel="stylesheet" href="https://fonts.googleapis.com/css2?family=Exo+2:wght@500;600;700;800&display=swap">
<style>
  :root {
    --brand-blue: #0255a3;
    --brand-red: #ec1f27;
    --brand-white: #ffffff;
    --brand-grey: #d3d3d3;
    --ink: #1e1e1e;
    --stage: #e9ebea;
  }
  * { box-sizing: border-box; margin: 0; padding: 0; }
  html, body {
    width: 1200px; height: 900px; overflow: hidden;
    background: var(--stage);
    font-family: "Exo 2", "Trebuchet MS", sans-serif;
  }
  .postcard {
    position: absolute;
    width: 530px; height: 376px;
    top: 262px;
    overflow: hidden;
    background: linear-gradient(180deg, var(--brand-white) 0%, #f4f4f4 55%, #dedede 100%);
    box-shadow: 0 6px 18px rgba(0,0,0,0.18);
  }
  .postcard--address { left: 50px; }
  .postcard--offer { left: 620px; background: var(--brand-white); }

  /* Wordmark */
  .wordmark { position: absolute; white-space: nowrap; }
  .wordmark__name {
    font-weight: 800; color: var(--brand-blue);
    font-size: 22px; line-height: 1; letter-spacing: 0.3px;
  }
  .wordmark__name::before {
    content: ""; display: inline-block;
    width: 14px; height: 14px; margin-right: 7px;
    background: var(--brand-red); border-radius: 50%;
    vertical-align: 1px;
  }
  .wordmark__trades {
    margin-top: 6px; font-size: 11px; font-weight: 600; color: var(--ink);
  }

  /* Address side */
  .postcard--address .wordmark { left: 40px; top: 160px; }
  .offer-stamp { position: absolute; left: 290px; top: 18px; width: 200px; height: 190px; }
  .address-box {
    position: absolute; left: 272px; top: 232px;
    width: 244px; height: 92px;
    border: 1px solid #444;
    padding: 14px 18px;
    font-size: 11px; font-weight: 700; color: var(--ink);
    line-height: 20px;
  }
  .address-box__zip { position: absolute; left: 150px; top: 34px; }
  .address-band {
    position: absolute; left: 0; right: 0; bottom: 0; height: 26px;
    background: var(--brand-blue);
  }

  /* Offer side */
  .postcard--offer .wordmark { left: 40px; top: 64px; }
  .trade-strip {
    position: absolute; left: 0; top: 150px; width: 288px; height: 50px;
    background: var(--brand-grey);
  }
  .trade-icon {
    position: absolute; top: 4px; width: 42px; height: 42px; border-radius: 50%;
    border: 2px solid var(--brand-white);
  }
  .trade-icon--plumbing { left: 44px; background: radial-gradient(circle at 40% 40%, #6fa7d9, var(--brand-blue)); }
  .trade-icon--electrical { left: 92px; background: radial-gradient(circle at 40% 40%, #f6f0e4, var(--brand-red)); }
  .trade-icon--hotwater { left: 140px; background: radial-gradient(circle at 40% 40%, #c9b9a6, #7b7b7b); }
  .offer-badge { position: absolute; left: 92px; top: 216px; width: 124px; height: 100px; }
  .tagline {
    position: absolute; left: 0; top: 325px; width: 288px;
    text-align: center; color: var(--brand-blue); font-weight: 800; line-height: 1.05;
  }
  .tagline__main { font-size: 14px; }
  .tagline__main small { font-size: 10.5px; }
  .tagline__sub { font-size: 9.5px; margin-top: 2px; }
  .accent-bar {
    position: absolute; left: 288px; top: 40px; width: 12px; height: 336px;
    background: var(--brand-red);
  }
  .hero-photo {
    position: absolute; left: 300px; top: 40px; width: 230px; height: 336px;
    background: linear-gradient(120deg, #6f675f 0%, #d9d6d2 30%, #f4f4f4 50%, #bcbcbc 70%, #5d554c 100%);
  }
  .hero-photo__band {
    position: absolute; left: 0; right: 0; top: 66px; height: 62px;
    background: rgba(255,255,255,0.35);
  }
</style>
</head>
<body>

<section class="postcard postcard--address" aria-label="Address side">
  <div class="wordmark">
    <div class="wordmark__name">Harbour Trades</div>
    <div class="wordmark__trades">Plumbing • Electrical • Hot Water</div>
  </div>

  <svg class="offer-stamp" viewBox="0 0 210 200" aria-label="Feel the love with $35 off your next job">
    <defs>
      <path id="stamp-arc-top" d="M40,100 A65,65 0 0 1 170,100"/>
      <path id="stamp-arc-bottom" d="M36,104 A69,69 0 0 0 174,104"/>
    </defs>
    <g transform="rotate(-14 105 100)">
      <circle cx="105" cy="100" r="86" fill="none" stroke="#ec1f27" stroke-width="6"/>
      <circle cx="105" cy="100" r="55" fill="none" stroke="#ec1f27" stroke-width="2"/>
      <text font-family="Exo 2, sans-serif" font-weight="700" font-size="13" fill="#ec1f27" letter-spacing="1">
        <textPath href="#stamp-arc-top" startOffset="50%" text-anchor="middle">FEEL THE LOVE WITH</textPath>
      </text>
      <text font-family="Exo 2, sans-serif" font-weight="700" font-size="13" fill="#ec1f27" letter-spacing="1" dominant-baseline="hanging">
        <textPath href="#stamp-arc-bottom" startOffset="50%" text-anchor="middle">YOUR NEXT JOB</textPath>
      </text>
      <rect x="8" y="80" width="194" height="40" fill="#ec1f27"/>
      <text x="105" y="112" text-anchor="middle" font-family="Exo 2, sans-serif" font-weight="800" font-size="34" fill="#ffffff">$35 OFF</text>
    </g>
  </svg>

  <div class="address-box">
    <div>JOHN SMITH</div>
    <div>ADRESS LINE 1</div>
    <div>ADRESS LINE 2</div>
    <span class="address-box__zip">ZIP CODE</span>
  </div>
  <div class="address-band"></div>
</section>

<section class="postcard postcard--offer" aria-label="Offer side">
  <div class="wordmark">
    <div class="wordmark__name">Harbour Trades</div>
    <div class="wordmark__trades">Plumbing • Electrical • Hot Water</div>
  </div>

  <div class="trade-strip">
    <span class="trade-icon trade-icon--plumbing" role="img" aria-label="Plumbing pipe icon"></span>
    <span class="trade-icon trade-icon--electrical" role="img" aria-label="Light bulb icon"></span>
    <span class="trade-icon trade-icon--hotwater" role="img" aria-label="Hot water tap icon"></span>
  </div>

  <svg class="offer-badge" viewBox="0 0 124 100" aria-label="Get off $35 or $XX next job">
    <path d="M4,4 H120 V60 Q120,88 62,98 Q4,88 4,60 Z" fill="#0255a3"/>
    <path d="M10,8 H114 V58 Q114,82 62,92 Q10,82 10,58 Z" fill="#ec1f27"/>
    <text x="62" y="30" text-anchor="middle" font-family="Exo 2, sans-serif" font-weight="600" font-size="11" fill="#ffffff">GET OFF</text>
    <text x="62" y="52" text-anchor="middle" font-family="Exo 2, sans-serif" font-weight="700" font-size="13" fill="#ffffff">$35 OR $XX</text>
    <text x="62" y="68" text-anchor="middle" font-family="Exo 2, sans-serif" font-weight="700" font-size="13" fill="#ffffff">NEXT JOB</text>
  </svg>

  <div class="tagline">
    <div class="tagline__main">CALL 1 NUMBER FOR THE BEST</div>
    <div class="tagline__main">IN 3 <small>TRADES</small></div>
    <div class="tagline__sub">PLUMBING, HOT WATER &amp; ELECTRICAL</div>
  </div>

  <div class="accent-bar"></div>
  <div class="hero-photo" role="img" aria-label="Close-up photo of a white radiator thermostat dial">
    <div class="hero-photo__band"></div>
  </div>
</section>

</body>
</html>
```